Web Developer Needs a Business Card Design

I need a personal business card design that represents me as a web developer for potential employers. I would like the background to be a dark color on the front for contrast with my logo and name. The back will have all my information along with a smaller version of the logo. I want something with a modern look and feel, not too conservative. This will be used for potential employers and freelance work.

Industry/Entity Type

Business

Contact Information for Business Card

Front should have my logo and name. The back should have all my personal information which would include: name: Tom Varnuch, phone: 570-614-9083, email: tomvarnuch@mailnest.example, website url: www.tomvarnuch.example, logo, web developer.

Font styles to use
Sans Serif

Requirements
Must have
• Must include my logo. The color palette base color will be the logo color.

```html
<!DOCTYPE html>
<html lang="en">
<head>
<meta charset="utf-8">
<title>Tom Varnuch — Business Card</title>
<link href="https://fonts.googleapis.com/css2?family=Arimo:wght@400;700&display=swap" rel="stylesheet">
<style>
  :root {
    --stage: #ecebe8;
    --card: #ffffff;
    --teal: #6cc5b5;
    --teal-light: #a6dbd1;
    --ink: #1b1b1b;
    --swoosh: #111111;
  }
  html, body {
    margin: 0;
    width: 1200px;
    height: 892px;
    overflow: hidden;
    background: var(--stage);
    font-family: "Arimo", Arial, sans-serif;
    color: var(--ink);
  }
  .card {
    position: absolute;
    width: 530px;
    height: 303px;
    background: var(--card);
    box-shadow: 0 10px 28px rgba(0,0,0,.18);
    overflow: hidden;
  }
  .card--front { left: 45px; top: 295px; }
  .card--back  { left: 625px; top: 295px; }

  /* front */
  .brand-mark {
    position: absolute;
    left: 0; right: 0; top: 72px;
    display: flex; align-items: center; justify-content: center; gap: 14px;
  }
  .brand-mark__dot {
    width: 26px; height: 26px; border-radius: 50%;
    background: var(--teal);
  }
  .brand-mark__name {
    font-weight: 700; font-size: 38px; color: var(--teal);
  }
  .front-name {
    position: absolute; left: 0; right: 0; bottom: 42px;
    text-align: center;
    font-weight: 700; font-size: 34px; letter-spacing: 1px;
  }

  /* back */
  .back-art { position: absolute; inset: 0; }
  .back-logo {
    position: absolute; right: 34px; top: 62px;
    display: flex; align-items: center; gap: 10px;
  }
  .back-logo__dot { width: 18px; height: 18px; border-radius: 50%; background: var(--teal); }
  .back-logo__name { font-weight: 700; font-size: 24px; color: var(--teal); }

  .identity { position: absolute; left: 26px; top: 38px; }
  .identity__name { font-size: 30px; font-weight: 400; margin: 0; line-height: 1.1; }
  .identity__role { font-size: 19px; margin: 4px 0 0 8px; }

  .divider {
    position: absolute; left: 118px; top: 208px;
    width: 1px; height: 80px; background: var(--ink);
  }
  .contacts {
    position: absolute; left: 134px; top: 212px;
    list-style: none; margin: 0; padding: 0;
    font-size: 16px; line-height: 25px;
  }
  .contacts li { display: flex; align-items: center; gap: 10px; }
  .contacts svg { width: 15px; height: 15px; flex: none; }
</style>
</head>
<body>

<section class="card card--front" aria-label="Card front">
  <div class="brand-mark">
    <span class="brand-mark__dot"></span>
    <span class="brand-mark__name">Tom Varnuch</span>
  </div>
  <div class="front-name">TOM VARNUCH</div>
</section>

<section class="card card--back" aria-label="Card back">
  <svg class="back-art" viewBox="0 0 530 303" preserveAspectRatio="none" aria-hidden="true">
    <defs>
      <linearGradient id="tealFade" x1="0" y1="0" x2="1" y2="1">
        <stop offset="0" stop-color="#a6dbd1"/>
        <stop offset="1" stop-color="#62c1b0"/>
      </linearGradient>
    </defs>
    <rect width="530" height="303" fill="url(#tealFade)"/>
    <path d="M250 0 C258 120 360 198 530 212 L530 0 Z" fill="#ffffff"/>
    <path d="M256 22 C272 140 370 198 512 209 C365 192 278 130 256 22 Z" fill="var(--swoosh)"/>
  </svg>

  <div class="back-logo">
    <span class="back-logo__dot"></span>
    <span class="back-logo__name">Tom Varnuch</span>
  </div>

  <div class="identity">
    <h1 class="identity__name">Tom Varnuch</h1>
    <p class="identity__role">Web Developer</p>
  </div>

  <div class="divider"></div>

  <ul class="contacts">
    <li>
      <svg viewBox="0 0 16 16" aria-hidden="true"><rect width="16" height="16" fill="#1b1b1b"/><path d="M5 3.5l2 2-1 1.2c.6 1.3 1.6 2.3 2.8 2.8L10 8.5l2 2-1.3 1.6C7.5 11.8 4.2 8.5 3.9 5.3Z" fill="#fff"/></svg>
      570-614-9083
    </li>
    <li>
      <svg viewBox="0 0 16 16" aria-hidden="true"><rect width="16" height="16" fill="#1b1b1b"/><rect x="3" y="4.5" width="10" height="7" fill="none" stroke="#fff" stroke-width="1.2"/><path d="M3 4.5l5 4 5-4" fill="none" stroke="#fff" stroke-width="1.2"/></svg>
      tomvarnuch@mailnest.example
    </li>
    <li>
      <svg viewBox="0 0 16 16" aria-hidden="true"><rect width="16" height="16" fill="#1b1b1b"/><circle cx="8" cy="8" r="4.8" fill="none" stroke="#fff" stroke-width="1.2"/><path d="M3.2 8h9.6M8 3.2c-2.4 3-2.4 6.6 0 9.6M8 3.2c2.4 3 2.4 6.6 0 9.6" fill="none" stroke="#fff" stroke-width="1"/></svg>
      www.tomvarnuch.example
    </li>
  </ul>
</section>

</body>
</html>
```